School learning environment project dashboard

We have an online learning enviroment for schools (12 / 18 year). Within this enviroment students work on projects.

Attached we have a setup we have created for a project, but we are looking for more ideas to make this even better, more sexy and still keep it functional for teachers and students.

The attached files show one dashboard we have. This dashboard holds the roadmap for the student, upcoming appointments, latest messages and the main documents the student is working on.

Target Market(s)

schools

Number of Pages Required

1 page

Font styles to use
Sans Serif

```html
<!DOCTYPE html>
<html lang="en">
<head>
<meta charset="utf-8">
<title>Project dashboard</title>
<link href="https://fonts.googleapis.com/css2?family=Montserrat:wght@400;500;600;700&display=swap" rel="stylesheet">
<style>
:root{
  --page:#efefef;
  --green:#4fbf26;
  --navy:#07182c;
  --sidebar:#051a2e;
  --main:#e3e6ee;
  --white:#ffffff;
  --ink:#14213a;
  --muted:#5c6678;
  --line:#d8dce5;
  --soft:#eef1f7;
  --blue:#1e7fe0;
  --tab-blue:#1b6fc4;
  --ok:#4fbf26;
  --ok-soft:#d8f0c9;
  --info:#2d8ee8;
  --info-soft:#cfe4f8;
  --warn:#f2cc2a;
  --warn-soft:#fbf0c2;
  --bad:#e42a3c;
  --bad-soft:#f9d6dc;
}
*{box-sizing:border-box;margin:0;padding:0}
html,body{width:1200px;height:4348px;overflow:hidden}
body{position:relative;background:var(--page);font-family:"Montserrat",sans-serif;color:var(--ink)}
.backdrop{position:absolute;left:0;top:0;width:1200px;height:800px}
.screen{position:absolute;left:79px;width:1042px;background:var(--main);box-shadow:0 6px 22px rgba(0,0,0,.25);overflow:hidden}
.topbar{position:absolute;left:0;top:0;width:100%;height:50px;background:var(--navy)}
.brand{position:absolute;left:16px;top:15px;display:flex;align-items:center;gap:7px;color:var(--white);font-weight:700;font-size:13px}
.brand i{width:12px;height:12px;background:var(--white);display:block}
.bell{position:absolute;left:858px;top:14px}
.logout{position:absolute;left:900px;top:12px;width:78px;height:25px;border:1px solid #c9d1dd;color:var(--white);font-size:8px;font-weight:600;display:flex;align-items:center;justify-content:center;gap:6px}
.logout b{width:9px;height:9px;background:var(--white);display:block}
.sidebar{position:absolute;left:0;top:50px;width:147px;bottom:0;background:var(--sidebar)}
.avatar{position:absolute;left:40px;top:18px;width:66px;height:66px;border-radius:50%;background:radial-gradient(circle at 50% 40%,#c8b6a4,#6d7a8c);border:2px solid #fff}
.welcome{position:absolute;left:0;top:92px;width:147px;text-align:center;color:var(--white);font-size:9px;font-weight:600;line-height:13px}
.nav{position:absolute;left:14px;top:149px;list-style:none}
.nav li{display:flex;align-items:center;gap:9px;height:39px;color:var(--white);font-size:9px;font-weight:600}
.nav li::before{content:"";width:17px;height:17px;border-radius:50%;background:var(--green);display:block}
.banner{position:absolute;left:187px;top:79px;width:799px;height:78px;background:linear-gradient(90deg,#0c1a2f 0%,#1b2a40 60%,#2a3950 80%,#13223a 100%)}
.banner h1{position:absolute;left:28px;top:18px;color:var(--white);font-size:15px;font-weight:700;letter-spacing:.3px}
.banner .crumbs{position:absolute;left:28px;top:42px;color:#c4ccd8;font-size:8px}
.banner .hide{position:absolute;right:28px;top:30px;color:#d8dee8;font-size:8px;display:flex;align-items:center;gap:7px}
.banner .hide i{width:15px;height:15px;border-radius:50%;background:var(--green);display:block}
.tabs{position:absolute;left:187px;top:177px;width:799px;height:37px;background:linear-gradient(90deg,#1a5aa6,#1f7cd2);display:flex;align-items:center}
.tab{height:100%;display:flex;align-items:center;padding:0 24px;color:var(--white);font-size:8px;font-weight:700;letter-spacing:.4px;width:110px}
.tab.active{background:var(--green)}
.tab-tools{position:absolute;right:24px;top:9px;display:flex;gap:12px}
.tab-tools i{width:21px;height:21px;border-radius:50%;background:var(--white);display:block}
.card{position:absolute;left:187px;top:214px;width:799px;background:var(--white)}
.title{position:absolute;font-size:14px;font-weight:700;color:var(--ink)}
.arrows{position:absolute;right:22px;top:35px;font-size:14px;font-weight:600;letter-spacing:6px}
.timeline{position:absolute;left:22px;top:81px;display:flex;gap:27px}
.step{position:relative;width:103px;height:118px;background:var(--white);box-shadow:0 2px 8px rgba(20,33,58,.14)}
.step + .step::before{content:"";position:absolute;left:-27px;top:54px;width:27px;border-top:1px dashed #8a93a3}
.step .num{position:absolute;left:26px;top:31px;width:51px;height:51px;border-radius:50%;display:flex;align-items:center;justify-content:center;font-size:15px;font-weight:700}
.step .badge{position:absolute;left:61px;top:19px;width:18px;height:18px;border-radius:50%;border:2px solid #fff}
.step .when{position:absolute;left:0;top:91px;width:100%;text-align:center;font-size:7.5px;font-weight:700}
.ok .num{background:var(--ok-soft);color:#2e7d12}.ok .badge{background:var(--ok)}
.info .num{background:var(--info-soft);color:#1b4f86}.info .badge{background:var(--info)}
.warn .num{background:var(--warn-soft);color:#7a5a00}.warn .badge{background:var(--warn)}
.bad .num{background:var(--bad-soft);color:#9c1a29}.bad .badge{background:var(--bad)}
.status{position:absolute;top:-27px;left:50%;transform:translateX(-50%);height:18px;padding:0 9px;border:1px solid var(--line);background:#fff;font-size:7.5px;color:var(--muted);display:flex;align-items:center;white-space:nowrap}
.status::after{content:"";position:absolute;left:50%;bottom:-5px;width:8px;height:8px;background:#fff;border-right:1px solid var(--line);border-bottom:1px solid var(--line);transform:translateX(-50%) rotate(45deg)}
.doc{position:absolute;left:22px;width:361px;height:59px;background:var(--white);box-shadow:0 2px 8px rgba(20,33,58,.14);display:flex;align-items:center}
.doc .ico{width:59px;height:59px;background:var(--soft);display:flex;align-items:center;justify-content:center}
.doc .name{margin-left:18px;font-size:10px;font-weight:700;flex:1}
.doc .acts{display:flex;gap:10px;margin-right:18px}
.doc .acts i{width:20px;height:20px;border-radius:50%;background:var(--soft);display:flex;align-items:center;justify-content:center}
.doc .acts i::after{content:"";width:8px;height:8px;background:var(--ink);border-radius:1px}
.viewall{position:absolute;left:700px;width:71px;height:19px;border:1px solid var(--line);font-size:7.5px;font-weight:700;display:flex;align-items:center;justify-content:center;box-shadow:0 1px 3px rgba(0,0,0,.1)}
.panel{position:absolute;left:412px;width:363px;background:var(--white);box-shadow:0 2px 8px rgba(20,33,58,.14)}
.appt{display:flex;align-items:center;height:64px;padding:0 18px 0 20px;border-bottom:1px solid #edf0f4}
.appt:last-child{border-bottom:0}
.appt .cal{width:37px;height:37px;background:var(--soft);display:flex;align-items:center;justify-content:center}
.appt .txt{flex:1;margin-left:20px;font-size:10px;line-height:15px}
.appt .txt b{font-weight:700;display:block;font-size:10px}
.appt .st{width:22px;height:22px;border-radius:50%}
.empty{height:59px;display:flex;align-items:center;padding-left:20px;font-size:10px;font-weight:500}
.post{padding:22px 20px}
.post .head{display:flex;justify-content:space-between;font-size:8px;font-weight:600}
.post .head span{font-weight:400;color:var(--muted)}
.post .body{display:flex;align-items:center;margin-top:10px}
.post .msg{width:278px;height:50px;background:#e8ebf5;font-size:8px;color:var(--muted);padding-left:15px;display:flex;align-items:center}
.post .pic{width:32px;height:32px;border-radius:50%;margin-left:12px;background:radial-gradient(circle at 50% 40%,#c8b6a4,#6d7a8c)}
.copyright{position:absolute;left:187px;width:799px;text-align:center;font-size:8.5px;color:var(--ink)}
.chat-fab{position:absolute;left:999px;width:34px;height:34px;border-radius:50%;background:var(--tab-blue);display:flex;align-items:center;justify-content:center;box-shadow:0 2px 6px rgba(0,0,0,.2)}
.popup{position:absolute;left:711px;top:662px;width:275px;height:295px;background:var(--blue);padding:0 17px}
.popup .ph{display:flex;align-items:center;gap:9px;height:40px;color:#fff;font-size:10px;font-weight:700}
.popup .ph i{width:20px;height:20px;border-radius:50%;background:#fff;display:block}
.popup .ph em{margin-left:auto;font-style:normal;font-size:13px}
.popup .field{background:#fff;height:32px;margin-top:9px;font-size:7.5px;color:var(--muted);padding:10px 14px}
.popup .field.area{height:93px}
.popup .submit{margin-top:16px;height:32px;background:#1c5db0;color:#fff;font-size:8px;font-weight:700;display:flex;align-items:center;justify-content:center}
</style>
</head>
<body>
<svg width="0" height="0" style="position:absolute">
  <defs>
    <symbol id="tick" viewBox="0 0 20 20"><path d="M5 10.5l3.2 3.2L15 7" fill="none" stroke="#fff" stroke-width="2.4" stroke-linecap="round" stroke-linejoin="round"/></symbol>
    <symbol id="cross" viewBox="0 0 20 20"><path d="M6.5 6.5l7 7M13.5 6.5l-7 7" stroke="#fff" stroke-width="2.4" stroke-linecap="round"/></symbol>
    <symbol id="pen" viewBox="0 0 20 20"><path d="M6 14l1-3 6-6 2 2-6 6z" fill="#fff"/></symbol>
    <symbol id="dots" viewBox="0 0 20 20"><circle cx="6" cy="10" r="1.5" fill="#fff"/><circle cx="10" cy="10" r="1.5" fill="#fff"/><circle cx="14" cy="10" r="1.5" fill="#fff"/></symbol>
    <symbol id="cal" viewBox="0 0 16 16"><rect x="1" y="3" width="14" height="12" rx="1" fill="#14213a"/><rect x="4" y="1" width="2" height="4" fill="#14213a"/><rect x="10" y="1" width="2" height="4" fill="#14213a"/><path d="M3 7h10v6H3z" fill="#eef1f7"/><path d="M4 8h2v2H4zM7 8h2v2H7zM10 8h2v2h-2zM4 11h2v1H4zM7 11h2v1H7z" fill="#14213a"/></symbol>
    <symbol id="file" viewBox="0 0 16 16"><path d="M3 1h7l4 4v10H3z" fill="#14213a"/><path d="M5 8h6M5 10h6M5 12h6" stroke="#eef1f7"/></symbol>
    <symbol id="chart" viewBox="0 0 16 16"><path d="M1 2v13h14" fill="none" stroke="#14213a" stroke-width="1.8"/><path d="M3 11l4-4 3 3 5-5" fill="none" stroke="#14213a" stroke-width="1.8"/></symbol>
    <symbol id="pie" viewBox="0 0 16 16"><path d="M7 2a6.5 6.5 0 1 0 7 7H7z" fill="#14213a"/><path d="M9 0.5v6.5h6.5A6.5 6.5 0 0 0 9 .5z" fill="#14213a"/></symbol>
    <symbol id="bell" viewBox="0 0 16 16"><path d="M8 1a4.5 4.5 0 0 0-4.5 4.5V10L2 12h12l-1.5-2V5.5A4.5 4.5 0 0 0 8 1zM6.5 13a1.5 1.5 0 0 0 3 0z" fill="#fff"/><circle cx="13" cy="3" r="2.6" fill="#4fbf26"/></symbol>
    <symbol id="bubble" viewBox="0 0 16 16"><path d="M2 3h9v6H6l-3 2.5V9H2z" fill="#fff"/><path d="M12 6h2v6h-1v2l-2.5-2H6v-1.5h6z" fill="#fff"/></symbol>
  </defs>
</svg>

<svg class="backdrop" viewBox="0 0 1200 800" aria-hidden="true"><polygon points="0,0 1120,0 0,768" fill="#4fbf26"/></svg>

<!-- Screen 1: default -->
<section class="screen" style="top:89px;height:1050px">
  <header class="topbar"><div class="brand"><i></i>Learnhub</div><svg class="bell" width="18" height="18"><use href="#bell"/></svg><div class="logout">LOG OUT<b></b></div></header>
  <aside class="sidebar"><div class="avatar" role="img" aria-label="Student profile photo"></div><p class="welcome">Welcome<br>Daniel Verhoeven</p>
    <ul class="nav"><li>Dashboard</li><li>Projects</li><li>Online</li><li>Profiles</li><li>App</li><li>Opportunities</li><li>Help</li></ul></aside>
  <div class="banner"><h1>EXAMPLE</h1><p class="crumbs">Dashboard &gt; Projects &gt; Profile paper Havo 2020-2021 &gt; Example</p><p class="hide"><i></i>Hide Menu</p></div>
  <nav class="tabs"><span class="tab active">PROGRESS</span><span class="tab">TOOLS</span><span class="tab">MESSAGES</span><div class="tab-tools"><i></i><i></i><i></i></div></nav>
  <div class="card" style="height:743px">
    <h2 class="title" style="left:22px;top:28px">Timeline</h2><span class="arrows">‹›</span>
    <div class="timeline">
      <div class="step ok"><svg class="badge"><use href="#tick"/></svg><span class="num">01</span><span class="when">00 MONTH</span></div>
      <div class="step ok"><svg class="badge"><use href="#tick"/></svg><span class="num">02</span><span class="when">00 MONTH</span></div>
      <div class="step ok"><svg class="badge"><use href="#tick"/></svg><span class="num">03</span><span class="when">00 MONTH</span></div>
      <div class="step info"><svg class="badge"><use href="#pen"/></svg><span class="num">04</span><span class="when">00 MONTH</span></div>
      <div class="step warn"><svg class="badge"><use href="#dots"/></svg><span class="num">05</span><span class="when">00 MONTH</span></div>
      <div class="step bad"><svg class="badge"><use href="#cross"/></svg><span class="num">06</span><span class="when">00 MONTH</span></div>
    </div>
    <h2 class="title" style="left:22px;top:238px">Documents</h2>
    <div class="doc" style="top:294px"><span class="ico"><svg width="20" height="20"><use href="#file"/></svg></span><span class="name">Paper</span><span class="acts"><i></i><i></i><i></i></span></div>
    <div class="doc" style="top:366px"><span class="ico"><svg width="20" height="20"><use href="#chart"/></svg></span><span class="name">Plan of action</span><span class="acts"><i></i><i></i><i></i></span></div>
    <div class="doc" style="top:444px"><span class="ico"><svg width="20" height="20"><use href="#pie"/></svg></span><span class="name">Powerpoint</span><span class="acts"><i></i><i></i><i></i></span></div>
    <h2 class="title" style="left:412px;top:238px">Upcomming appointments</h2><span class="viewall" style="top:238px">View all ›</span>
    <div class="panel" style="top:294px;height:211px;padding-top:6px">
      <div class="appt"><span class="cal"><svg width="16" height="16"><use href="#cal"/></svg></span><p class="txt"><b>Submitting research proposal</b>00 Month</p><svg class="st" style="background:var(--ok)"><use href="#tick"/></svg></div>
      <div class="appt"><span class="cal"><svg width="16" height="16"><use href="#cal"/></svg></span><p class="txt"><b>Example</b>00 Month</p><svg class="st" style="background:var(--warn)"><use href="#dots"/></svg></div>
      <div class="appt"><span class="cal"><svg width="16" height="16"><use href="#cal"/></svg></span><p class="txt"><b>Evaluation</b>00 Month</p><svg class="st" style="background:var(--bad)"><use href="#cross"/></svg></div>
    </div>
    <h2 class="title" style="left:412px;top:532px">Recent posts</h2><span class="viewall" style="top:532px">View all ›</span>
    <div class="panel post" style="top:587px;height:123px"><p class="head">Joris Brandsma<span>4-02-2021 at 19:39</span></p><div class="body"><p class="msg">Example message</p><span class="pic" role="img" aria-label="Author profile photo"></span></div></div>
  </div>
  <p class="copyright" style="top:996px">Copyright © Learnhub. 2021. All rights reserved.</p>
  <div class="chat-fab" style="top:918px"><svg width="16" height="16"><use href="#bubble"/></svg></div>
</section>

<!-- Screen 2: status labels -->
<section class="screen" style="top:1180px;height:1050px">
  <header class="topbar"><div class="brand"><i></i>Learnhub</div><svg class="bell" width="18" height="18"><use href="#bell"/></svg><div class="logout">LOG OUT<b></b></div></header>
  <aside class="sidebar"><div class="avatar" role="img" aria-label="Student profile photo"></div><p class="welcome">Welcome<br>Daniel Verhoeven</p>
    <ul class="nav"><li>Dashboard</li><li>Projects</li><li>Online</li><li>Profiles</li><li>App</li><li>Opportunities</li><li>Help</li></ul></aside>
  <div class="banner"><h1>EXAMPLE</h1><p class="crumbs">Dashboard &gt; Projects &gt; Profile paper Havo 2020-2021 &gt; Example</p><p class="hide"><i></i>Hide Menu</p></div>
  <nav class="tabs"><span class="tab active">PROGRESS</span><span class="tab">TOOLS</span><span class="tab">MESSAGES</span><div class="tab-tools"><i></i><i></i><i></i></div></nav>
  <div class="card" style="height:743px">
    <h2 class="title" style="left:22px;top:28px">Timeline</h2><span class="arrows">‹›</span>
    <div class="timeline">
      <div class="step ok"><svg class="badge"><use href="#tick"/></svg><span class="num">01</span><span class="when">00 MONTH</span></div>
      <div class="step ok"><svg class="badge"><use href="#tick"/></svg><span class="num">02</span><span class="when">00 MONTH</span></div>
      <div class="step ok"><span class="status">Approved</span><svg class="badge"><use href="#tick"/></svg><span class="num">03</span><span class="when">00 MONTH</span></div>
      <div class="step info"><span class="status">On Going</span><svg class="badge"><use href="#pen"/></svg><span class="num">04</span><span class="when">00 MONTH</span></div>
      <div class="step warn"><span class="status">On Hold</span><svg class="badge"><use href="#dots"/></svg><span class="num">05</span><span class="when">00 MONTH</span></div>
      <div class="step bad"><span class="status">Declined</span><svg class="badge"><use href="#cross"/></svg><span class="num">06</span><span class="when">00 MONTH</span></div>
    </div>
    <h2 class="title" style="left:22px;top:238px">Documents</h2>
    <div class="doc" style="top:294px"><span class="ico"><svg width="20" height="20"><use href="#file"/></svg></span><span class="name">Paper</span><span class="acts"><i></i><i></i><i></i></span></div>
    <div class="doc" style="top:366px"><span class="ico"><svg width="20" height="20"><use href="#chart"/></svg></span><span class="name">Plan of action</span><span class="acts"><i></i><i></i><i></i></span></div>
    <div class="doc" style="top:444px"><span class="ico"><svg width="20" height="20"><use href="#pie"/></svg></span><span class="name">Powerpoint</span><span class="acts"><i></i><i></i><i></i></span></div>
    <h2 class="title" style="left:412px;top:238px">Upcomming appointments</h2><span class="viewall" style="top:238px">View all ›</span>
    <div class="panel" style="top:294px;height:211px;padding-top:6px">
      <div class="appt"><span class="cal"><svg width="16" height="16"><use href="#cal"/></svg></span><p class="txt"><b>Submitting research proposal</b>00 Month</p><svg class="st" style="background:var(--ok)"><use href="#tick"/></svg></div>
      <div class="appt"><span class="cal"><svg width="16" height="16"><use href="#cal"/></svg></span><p class="txt"><b>Example</b>00 Month</p><svg class="st" style="background:var(--warn)"><use href="#dots"/></svg></div>
      <div class="appt"><span class="cal"><svg width="16" height="16"><use href="#cal"/></svg></span><p class="txt"><b>Evaluation</b>00 Month</p><svg class="st" style="background:var(--bad)"><use href="#cross"/></svg></div>
    </div>
    <h2 class="title" style="left:412px;top:532px">Recent posts</h2><span class="viewall" style="top:532px">View all ›</span>
    <div class="panel post" style="top:587px;height:123px"><p class="head">Joris Brandsma<span>4-02-2021 at 19:39</span></p><div class="body"><p class="msg">Example message</p><span class="pic" role="img" aria-label="Author profile photo"></span></div></div>
  </div>
  <p class="copyright" style="top:996px">Copyright © Learnhub. 2021. All rights reserved.</p>
  <div class="chat-fab" style="top:918px"><svg width="16" height="16"><use href="#bubble"/></svg></div>
</section>

<!-- Screen 3: message form open -->
<section class="screen" style="top:2277px;height:1050px">
  <header class="topbar"><div class="brand"><i></i>Learnhub</div><svg class="bell" width="18" height="18"><use href="#bell"/></svg><div class="logout">LOG OUT<b></b></div></header>
  <aside class="sidebar"><div class="avatar" role="img" aria-label="Student profile photo"></div><p class="welcome">Welcome<br>Daniel Verhoeven</p>
    <ul class="nav"><li>Dashboard</li><li>Projects</li><li>Online</li><li>Profiles</li><li>App</li><li>Opportunities</li><li>Help</li></ul></aside>
  <div class="banner"><h1>EXAMPLE</h1><p class="crumbs">Dashboard &gt; Projects &gt; Profile paper Havo 2020-2021 &gt; Example</p><p class="hide"><i></i>Hide Menu</p></div>
  <nav class="tabs"><span class="tab active">PROGRESS</span><span class="tab">TOOLS</span><span class="tab">MESSAGES</span><div class="tab-tools"><i></i><i></i><i></i></div></nav>
  <div class="card" style="height:743px">
    <h2 class="title" style="left:22px;top:28px">Timeline</h2><span class="arrows">‹›</span>
    <div class="timeline">
      <div class="step ok"><svg class="badge"><use href="#tick"/></svg><span class="num">01</span><span class="when">00 MONTH</span></div>
      <div class="step ok"><svg class="badge"><use href="#tick"/></svg><span class="num">02</span><span class="when">00 MONTH</span></div>
      <div class="step ok"><svg class="badge"><use href="#tick"/></svg><span class="num">03</span><span class="when">00 MONTH</span></div>
      <div class="step info"><svg class="badge"><use href="#pen"/></svg><span class="num">04</span><span class="when">00 MONTH</span></div>
      <div class="step warn"><svg class="badge"><use href="#dots"/></svg><span class="num">05</span><span class="when">00 MONTH</span></div>
      <div class="step bad"><svg class="badge"><use href="#cross"/></svg><span class="num">06</span><span class="when">00 MONTH</span></div>
    </div>
    <h2 class="title" style="left:22px;top:238px">Documents</h2>
    <div class="doc" style="top:294px"><span class="ico"><svg width="20" height="20"><use href="#file"/></svg></span><span class="name">Paper</span><span class="acts"><i></i><i></i><i></i></span></div>
    <div class="doc" style="top:366px"><span class="ico"><svg width="20" height="20"><use href="#chart"/></svg></span><span class="name">Plan of action</span><span class="acts"><i></i><i></i><i></i></span></div>
    <div class="doc" style="top:444px"><span class="ico"><svg width="20" height="20"><use href="#pie"/></svg></span><span class="name">Powerpoint</span><span class="acts"><i></i><i></i><i></i></span></div>
    <h2 class="title" style="left:412px;top:238px">Upcomming appointments</h2><span class="viewall" style="top:238px">View all ›</span>
    <div class="panel" style="top:294px;height:211px;padding-top:6px">
      <div class="appt"><span class="cal"><svg width="16" height="16"><use href="#cal"/></svg></span><p class="txt"><b>Submitting research proposal</b>00 Month</p><svg class="st" style="background:var(--ok)"><use href="#tick"/></svg></div>
      <div class="appt"><span class="cal"><svg width="16" height="16"><use href="#cal"/></svg></span><p class="txt"><b>Example</b>00 Month</p><svg class="st" style="background:var(--warn)"><use href="#dots"/></svg></div>
      <div class="appt"><span class="cal"><svg width="16" height="16"><use href="#cal"/></svg></span><p class="txt"><b>Evaluation</b>00 Month</p><svg class="st" style="background:var(--bad)"><use href="#cross"/></svg></div>
    </div>
    <h2 class="title" style="left:412px;top:532px">Recent posts</h2><span class="viewall" style="top:532px">View all ›</span>
    <div class="panel post" style="top:587px;height:123px"><p class="head">Joris Brandsma<span>4-02-2021 at 19:39</span></p><div class="body"><p class="msg">Example message</p><span class="pic" role="img" aria-label="Author profile photo"></span></div></div>
  </div>
  <form class="popup"><p class="ph"><i></i>Leave a Message<em>×</em></p>
    <p class="field">Your Name (Required)</p><p class="field">Your Email (Required)</p><p class="field area">Your Message</p><p class="submit">SUBMIT</p></form>
  <p class="copyright" style="top:996px">Copyright © Learnhub. 2021. All rights reserved.</p>
  <div class="chat-fab" style="top:918px"><svg width="16" height="16"><use href="#bubble"/></svg></div>
</section>

<!-- Screen 4: empty states -->
<section class="screen" style="top:3388px;height:871px">
  <header class="topbar"><div class="brand"><i></i>Learnhub</div><svg class="bell" width="18" height="18"><use href="#bell"/></svg><div class="logout">LOG OUT<b></b></div></header>
  <aside class="sidebar"><div class="avatar" role="img" aria-label="Student profile photo"></div><p class="welcome">Welcome<br>Daniel Verhoeven</p>
    <ul class="nav"><li>Dashboard</li><li>Projects</li><li>Online</li><li>Profiles</li><li>App</li><li>Opportunities</li><li>Help</li></ul></aside>
  <div class="banner"><h1>EXAMPLE</h1><p class="crumbs">Dashboard &gt; Projects &gt; Profile paper Havo 2020-2021 &gt; Example</p><p class="hide"><i></i>Hide Menu</p></div>
  <nav class="tabs"><span class="tab active">PROGRESS</span><span class="tab">TOOLS</span><span class="tab">MESSAGES</span><div class="tab-tools"><i></i><i></i><i></i></div></nav>
  <div class="card" style="height:573px">
    <h2 class="title" style="left:22px;top:28px">Timeline</h2><span class="arrows">‹›</span>
    <div class="timeline">
      <div class="step ok"><svg class="badge"><use href="#tick"/></svg><span class="num">01</span><span class="when">00 MONTH</span></div>
      <div class="step ok"><svg class="badge"><use href="#tick"/></svg><span class="num">02</span><span class="when">00 MONTH</span></div>
      <div class="step ok"><svg class="badge"><use href="#tick"/></svg><span class="num">03</span><span class="when">00 MONTH</span></div>
      <div class="step info"><svg class="badge"><use href="#pen"/></svg><span class="num">04</span><span class="when">00 MONTH</span></div>
      <div class="step warn"><svg class="badge"><use href="#dots"/></svg><span class="num">05</span><span class="when">00 MONTH</span></div>
      <div class="step bad"><svg class="badge"><use href="#cross"/></svg><span class="num">06</span><span class="when">00 MONTH</span></div>
    </div>
    <h2 class="title" style="left:22px;top:238px">Documents</h2>
    <div class="doc" style="top:294px"><span class="ico"><svg width="20" height="20"><use href="#file"/></svg></span><span class="name">Paper</span><span class="acts"><i></i><i></i><i></i></span></div>
    <div class="doc" style="top:366px"><span class="ico"><svg width="20" height="20"><use href="#chart"/></svg></span><span class="name">Plan of action</span><span class="acts"><i></i><i></i><i></i></span></div>
    <div class="doc" style="top:444px"><span class="ico"><svg width="20" height="20"><use href="#pie"/></svg></span><span class="name">Powerpoint</span><span class="acts"><i></i><i></i><i></i></span></div>
    <h2 class="title" style="left:412px;top:238px">Upcomming appointments</h2><span class="viewall" style="top:238px">View all ›</span>
    <div class="panel" style="top:294px"><p class="empty">No appointments to show you at the moment</p></div>
    <h2 class="title" style="left:412px;top:394px">Recent posts</h2><span class="viewall" style="top:394px">View all ›</span>
    <div class="panel" style="top:449px"><p class="empty">No message to show you at the moment</p></div>
  </div>
  <p class="copyright" style="top:826px">Copyright © Learnhub. 2021. All rights reserved.</p>
  <div class="chat-fab" style="top:748px"><svg width="16" height="16"><use href="#bubble"/></svg></div>
</section>
</body>
</html>
```